business card and flyer/pricelist

Business Name: Willow Strand Salon
new boutique salon run from home, using Australian owned natural products and colours, we need a flyer design to do a letter box drop to advertise the business as well as incorporating a price list on the front (single sided with writing on front and only colour on back)

The salon has a natural feel with light coloured timber chairs, bamboo timber bench top and shelving.

we are after a natural toned colour for the flyer, with possibly a brown/darkish colour writing

we are after a flyer that will also be able to use the design heading (business name) for business cards as well

feel free to look on my pintrest account to get a feel for my style under Corinne Belvane.

I love simple clean and Natural looks.

Industry/Entity Type

Boutique

Font styles to use
Script
Other font styles liked:
• SCRIPT HANDWRITTEN FONTS

Colors
cadf82
e9f1ce
5c5c5c
d3d3d3
add136
fee18a

Requirements
Must have
• NATURAL COLOURINGS, eg soft greens, browns,
white or off white background.
Should not have
• photos,

```html
<!DOCTYPE html>
<html lang="en">
<head>
<meta charset="utf-8">
<title>Willow Strand Salon – Flyer and Price List</title>
<link rel="stylesheet" href="https://fonts.googleapis.com/css2?family=Dancing+Script:wght@600&family=Didact+Gothic&display=swap">
<style>
  :root {
    --page: #ffffff;
    --frame-edge: #d3d3d3;
    --leaf: #add136;
    --leaf-deep: #8fae24;
    --sage: #cadf82;
    --mist: #e9f1ce;
    --cream: #fbfcf4;
    --honey: #fee18a;
    --bark: #5a3e2b;
    --bark-soft: #7a5a42;
    --stone: #5c5c5c;
  }
  html, body {
    margin: 0;
    padding: 0;
    width: 1200px;
    height: 2609px;
    overflow: hidden;
    background: var(--page);
  }
  .flyer {
    position: absolute;
    left: 42px;
    top: 46px;
    width: 1120px;
    height: 2515px;
    border-radius: 22px;
    overflow: hidden;
    box-shadow: 0 0 0 2px var(--frame-edge);
    font-family: "Didact Gothic", "Century Gothic", sans-serif;
    color: var(--bark);
    background: var(--cream);
  }
  .brand-name {
    position: absolute;
    left: 0; right: 0;
    margin: 0;
    text-align: center;
    font-family: "Dancing Script", cursive;
    font-weight: 600;
    color: var(--bark);
    white-space: nowrap;
    line-height: 1;
  }
  .header {
    position: absolute;
    left: 0; top: 0;
    width: 100%;
    height: 298px;
    background:
      radial-gradient(ellipse 460px 260px at 160px 290px, rgba(254,225,138,0.55) 0%, rgba(254,225,138,0) 100%),
      linear-gradient(180deg, var(--sage) 0%, var(--leaf) 100%);
  }
  .header .brand-name {
    top: 92px;
    font-size: 104px;
  }
  .price-list {
    position: absolute;
    left: 0; top: 298px;
    width: 100%;
    height: 1889px;
    box-sizing: border-box;
    padding: 100px 110px 80px;
    background: linear-gradient(180deg, var(--cream) 0%, var(--mist) 100%);
  }
  .price-title {
    margin: 0;
    text-align: center;
    font-family: "Dancing Script", cursive;
    font-weight: 600;
    font-size: 120px;
    line-height: 130px;
    color: var(--bark);
  }
  .price-intro {
    margin: 14px 0 70px;
    text-align: center;
    font-size: 40px;
    line-height: 56px;
    color: var(--stone);
  }
  .price-group { margin: 0 0 64px; }
  .price-group:last-child { margin-bottom: 0; }
  .group-title {
    margin: 0 0 18px;
    padding-bottom: 12px;
    border-bottom: 3px solid var(--leaf);
    font-family: "Dancing Script", cursive;
    font-weight: 600;
    font-size: 76px;
    line-height: 86px;
    color: var(--leaf-deep);
  }
  .price-row {
    display: flex;
    align-items: baseline;
    font-size: 46px;
    line-height: 78px;
    color: var(--bark);
  }
  .price-row .item { white-space: nowrap; }
  .price-row .leader {
    flex: 1;
    margin: 0 18px;
    border-bottom: 3px dotted var(--bark-soft);
    transform: translateY(-10px);
  }
  .price-row .cost { white-space: nowrap; }
  .contact-band {
    position: absolute;
    left: 0; top: 2187px;
    width: 100%;
    height: 230px;
    background: var(--sage);
    color: var(--bark);
    font-size: 60px;
    line-height: 64px;
  }
  .contact-owner {
    position: absolute;
    left: 61px;
    top: 24px;
  }
  .contact-reach {
    position: absolute;
    right: 49px;
    top: 24px;
    text-align: right;
  }
  .contact-line { display: block; white-space: nowrap; }
  .footer {
    position: absolute;
    left: 0; top: 2417px;
    width: 100%;
    height: 98px;
    background: var(--leaf);
  }
  .footer .brand-name {
    top: 12px;
    font-size: 78px;
  }
</style>
</head>
<body>
  <main class="flyer">
    <header class="header">
      <h1 class="brand-name">Willow Strand Salon</h1>
    </header>

    <section class="price-list">
      <h2 class="price-title">Price List</h2>
      <p class="price-intro">Australian owned natural products and colours</p>

      <div class="price-group">
        <h3 class="group-title">Cuts</h3>
        <div class="price-row"><span class="item">Ladies Cut &amp; Blow Dry</span><span class="leader"></span><span class="cost">$55</span></div>
        <div class="price-row"><span class="item">Mens Cut</span><span class="leader"></span><span class="cost">$30</span></div>
        <div class="price-row"><span class="item">Childrens Cut</span><span class="leader"></span><span class="cost">$20</span></div>
        <div class="price-row"><span class="item">Fringe Trim</span><span class="leader"></span><span class="cost">$10</span></div>
      </div>

      <div class="price-group">
        <h3 class="group-title">Colour</h3>
        <div class="price-row"><span class="item">Full Colour</span><span class="leader"></span><span class="cost">from $85</span></div>
        <div class="price-row"><span class="item">Regrowth Colour</span><span class="leader"></span><span class="cost">from $65</span></div>
        <div class="price-row"><span class="item">Half Head Foils</span><span class="leader"></span><span class="cost">from $95</span></div>
        <div class="price-row"><span class="item">Full Head Foils</span><span class="leader"></span><span class="cost">from $140</span></div>
      </div>

      <div class="price-group">
        <h3 class="group-title">Styling</h3>
        <div class="price-row"><span class="item">Blow Dry</span><span class="leader"></span><span class="cost">$35</span></div>
        <div class="price-row"><span class="item">Up Style</span><span class="leader"></span><span class="cost">from $60</span></div>
        <div class="price-row"><span class="item">Treatment</span><span class="leader"></span><span class="cost">$25</span></div>
        <div class="price-row"><span class="item">Straighten or Curl</span><span class="leader"></span><span class="cost">$30</span></div>
      </div>
    </section>

    <section class="contact-band">
      <div class="contact-owner">
        <span class="contact-line">Owners Name</span>
        <span class="contact-line">Address</span>
      </div>
      <div class="contact-reach">
        <span class="contact-line">Phone: 123456</span>
        <span class="contact-line">email@website.com</span>
      </div>
    </section>

    <footer class="footer">
      <p class="brand-name">Willow Strand Salon</p>
    </footer>
  </main>
</body>
</html>
```